Business Card *

A business card design
Use the logo uploaded in the brief page.
You may use placeholders in your design layouts.
I will provide the actual business card details to the winning designer.

Logo
Place for contact info (name, title, phone, email, etc)

Requirements
Must have
• Logo

```html
<!DOCTYPE html>
<html lang="en">
<head>
<meta charset="utf-8">
<title>Harrowfield Business Card</title>
<link rel="stylesheet" href="https://fonts.googleapis.com/css2?family=Open+Sans:wght@400;600&display=swap">
<style>
  :root {
    --page-bg: #e3e3e3;
    --card-dark: #505154;
    --card-light: #f4f4f4;
    --brand-gray: #98999c;
    --accent-green: #3cae49;
    --text-dark: #444548;
    --shape-gray: #8c8d90;
  }
  * { margin: 0; padding: 0; box-sizing: border-box; }
  html, body { width: 1200px; height: 960px; overflow: hidden; }
  body {
    background: var(--page-bg);
    position: relative;
    font-family: "Open Sans", Arial, sans-serif;
  }
  .card {
    position: absolute;
    left: 305px;
    width: 592px;
    height: 337px;
    overflow: hidden;
    box-shadow: 3px 4px 6px rgba(0,0,0,0.35);
  }
  .card--front { top: 129px; background: var(--card-dark); }
  .card--back { top: 518px; height: 338px; background: var(--card-light); }

  .deco-circle {
    position: absolute;
    border-radius: 50%;
    background: var(--shape-gray);
  }
  .card--front .deco-circle { left: -80px; top: 80px; width: 170px; height: 170px; opacity: 0.55; }
  .card--back .deco-circle { right: -70px; top: 80px; width: 220px; height: 220px; opacity: 0.45; }

  .brand-name {
    font-family: "Open Sans", Arial, sans-serif;
    font-weight: 600;
    color: var(--brand-gray);
    line-height: 1;
  }
  .front-brand {
    position: absolute;
    left: 228px;
    top: 148px;
    width: 310px;
    text-align: center;
    font-size: 36px;
  }

  .back-brand {
    position: absolute;
    left: 40px;
    top: 30px;
    width: 182px;
    text-align: center;
  }
  .brand-dot {
    display: block;
    width: 58px;
    height: 58px;
    margin: 0 auto 14px;
    border-radius: 50%;
    background: var(--brand-gray);
  }
  .back-brand .brand-name { font-size: 24px; }

  .contact {
    position: absolute;
    left: 41px;
    top: 160px;
    color: var(--text-dark);
  }
  .contact-name { font-size: 18px; font-weight: 600; color: var(--accent-green); line-height: 24px; }
  .contact-title { font-size: 14px; line-height: 20px; }
  .contact-list { list-style: none; margin-top: 18px; }
  .contact-list li {
    font-size: 14px;
    line-height: 20px;
    display: flex;
    align-items: center;
    gap: 6px;
  }
  .contact-list svg { width: 13px; height: 13px; fill: var(--accent-green); flex: none; }
  .contact-address { font-size: 14px; line-height: 20px; margin-top: 7px; }
</style>
</head>
<body>
  <section class="card card--front" aria-label="Card front">
    <div class="deco-circle"></div>
    <div class="front-brand brand-name">Harrowfield</div>
  </section>

  <section class="card card--back" aria-label="Card back">
    <div class="deco-circle"></div>
    <div class="back-brand">
      <span class="brand-dot"></span>
      <div class="brand-name">Harrowfield</div>
    </div>
    <div class="contact">
      <div class="contact-name">Daniel Reyes</div>
      <div class="contact-title">Founder</div>
      <ul class="contact-list">
        <li>
          <svg viewBox="0 0 16 16" aria-hidden="true"><path d="M3.6 1.2l2.3 2.6-1.3 2.1c.9 2 2.4 3.5 4.4 4.4l2.1-1.3 2.6 2.3-1.3 2.4C7 13.4 2.6 9 1.2 2.5z"/></svg>
          (555) 018-2240
        </li>
        <li>
          <svg viewBox="0 0 16 16" aria-hidden="true"><path d="M1 3h14v10H1zM2.5 4.5v.4L8 9l5.5-4.1v-.4zM2.5 6.7v4.8h11V6.7L8 10.8z"/></svg>
          daniel@harrowfieldagri.com
        </li>
        <li>
          <svg viewBox="0 0 16 16" aria-hidden="true"><path d="M8 1a7 7 0 1 0 0 14A7 7 0 0 0 8 1zm0 1.5c.8.8 1.4 2.2 1.6 3.8H6.4C6.6 4.7 7.2 3.3 8 2.5zM2.6 7.5h2.3c0 .4 0 .7.1 1H2.6a5 5 0 0 1 0-1zm.5-1.2a5.6 5.6 0 0 1 2.7-3.2c-.5.9-.8 2-.9 3.2zm3.3 1.2h3.2v1H6.4zm4.7 0h2.3a5 5 0 0 1 0 1H11zm1.8-1.2H11c-.1-1.2-.4-2.3-.9-3.2a5.6 5.6 0 0 1 2.8 3.2zM3.1 9.7h1.8c.1 1.2.4 2.3.9 3.2a5.6 5.6 0 0 1-2.7-3.2zm3.3 0h3.2c-.2 1.6-.8 3-1.6 3.8-.8-.8-1.4-2.2-1.6-3.8zm4.7 0h1.8a5.6 5.6 0 0 1-2.7 3.2c.5-.9.8-2 .9-3.2z"/></svg>
          www.harrowfieldagri.com
        </li>
      </ul>
      <div class="contact-address">240 Orchard Lane, Suite 1200, Tampa, Florida, 33602</div>
    </div>
  </section>
</body>
</html>
```